Business Card for Ferncliff Massage

I need a business card for my massage therapy & cannabis oil practice. I already have a logo,the "massage" got edited out of this file. I will send the original soon. I need these elements to be on the card:
web: FerncliffMassage.example
ph: 541/382-9147
email: Marla.Quintavelle@mailbox.example
Other slogans, statements to consider:
Science Geek, Massage Therapist, Neuromuscular Therapy, Cannabis Spa Treatments, Raindrop Therapy, Essential Oils
Target Market(s)
women between 20 & 65, people with enough $ to afford regular massage, people who recently had a motor vehicle accident, Halvora HMC insured
Industry/Entity Type
Massage Therapy
Contact Information for Business Card
I would like to see my bear logo featured; contact details, greens & blues preferred colors.

```html
<!DOCTYPE html>
<html lang="en">
<head>
<meta charset="utf-8">
<title>Ferncliff Massage – Business Card</title>
<link href="https://fonts.googleapis.com/css2?family=Roboto:ital,wght@0,300;0,400;0,700;1,300&display=swap" rel="stylesheet">
<style>
  :root {
    --green: #2e7d3a;
    --brown: #73655a;
    --taupe: #a08a7c;
    --white: #ffffff;
    --backdrop: #5a5a5a;
  }
  * { box-sizing: border-box; margin: 0; padding: 0; }
  html, body { width: 1200px; height: 1200px; overflow: hidden; }
  body {
    background: var(--backdrop);
    font-family: "Roboto", Arial, sans-serif;
    position: relative;
  }
  .card {
    position: absolute;
    left: 256px;
    width: 686px;
    height: 390px;
    border-radius: 18px;
    overflow: hidden;
    background: var(--white);
  }
  .card--appointment { top: 192px; }
  .card--contact { top: 618px; }

  /* Appointment side */
  .appointment-band {
    position: absolute; left: 0; top: 0; bottom: 0; width: 58px;
    background: var(--green);
  }
  .appointment-band__label {
    position: absolute; left: 29px; top: 195px;
    transform: translate(-50%, -50%) rotate(-90deg);
    white-space: nowrap;
    color: var(--white); font-weight: 700; font-size: 25px; letter-spacing: 0.5px;
  }
  .appointment-body { position: absolute; inset: 0; color: var(--green); }
  .line { position: absolute; left: 0; width: 732px; text-align: center; font-size: 16px; font-weight: 300; }
  .line--brand { top: 28px; font-weight: 700; }
  .line--addr1 { top: 48px; }
  .line--addr2 { top: 68px; }
  .line--svc1 { top: 105px; }
  .line--svc2 { top: 125px; }
  .line--note1 { top: 327px; font-style: italic; }
  .line--note2 { top: 346px; font-style: italic; }
  .days {
    position: absolute; top: 171px; left: 94px; width: 544px;
    display: flex; justify-content: space-between;
    font-size: 16px; font-weight: 400;
  }
  .day { display: flex; align-items: center; gap: 4px; }
  .day__box { width: 15px; height: 15px; border: 1.5px solid var(--green); }
  .booking-row {
    position: absolute; left: 142px;
    display: flex; align-items: flex-end; gap: 6px;
    font-size: 16px;
  }
  .booking-row--first { top: 235px; }
  .booking-row--second { top: 280px; }
  .booking-row__blank { width: 140px; border-bottom: 1.5px solid var(--green); margin-bottom: 3px; margin-right: 10px; }

  /* Contact side */
  .contact-shape { position: absolute; inset: 0; }
  .brand-mark {
    position: absolute; left: 40px; top: 110px; width: 260px;
    display: flex; flex-direction: column; align-items: center; gap: 14px;
  }
  .brand-mark__dot { width: 70px; height: 70px; border-radius: 50%; background: var(--taupe); }
  .brand-mark__name { font-size: 50px; font-weight: 400; color: var(--green); }
  .person { position: absolute; right: 38px; text-align: right; color: var(--white); }
  .person__name { top: 168px; font-size: 26px; font-weight: 700; }
  .person__title { top: 200px; font-size: 18px; }
  .contact-list { position: absolute; right: 38px; top: 256px; list-style: none; color: var(--white); }
  .contact-list li {
    display: flex; justify-content: flex-end; align-items: center; gap: 9px;
    height: 23px; font-size: 16px;
  }
  .contact-list li.contact--email { font-size: 15px; }
  .contact-list svg { width: 18px; height: 16px; fill: none; stroke: var(--white); stroke-width: 1.6; }
  .person__license { top: 344px; font-size: 18px; }
</style>
</head>
<body>

<section class="card card--appointment">
  <div class="appointment-band"><span class="appointment-band__label">YOUR APPOINTMENT</span></div>
  <div class="appointment-body">
    <p class="line line--brand">Ferncliff</p>
    <p class="line line--addr1">2840 NW Alder Ridge Rd</p>
    <p class="line line--addr2">Bend, OR 97703, USA</p>
    <p class="line line--svc1">Science Geek, Massage Therapist, Neuromuscular Therapy</p>
    <p class="line line--svc2">Cannabis Spa Treatments, Raindrop Therapy, Essential Oils</p>
    <div class="days">
      <span class="day"><span class="day__box"></span>MON</span>
      <span class="day"><span class="day__box"></span>TUES</span>
      <span class="day"><span class="day__box"></span>WEDS</span>
      <span class="day"><span class="day__box"></span>THURS</span>
      <span class="day"><span class="day__box"></span>FRI</span>
      <span class="day"><span class="day__box"></span>SAT</span>
    </div>
    <div class="booking-row booking-row--first">DATE <span class="booking-row__blank"></span>TIME <span class="booking-row__blank"></span>am/pm</div>
    <div class="booking-row booking-row--second">DATE <span class="booking-row__blank"></span>TIME <span class="booking-row__blank"></span>am/pm</div>
    <p class="line line--note1">This time reserved for you. If possible to keep this appointment,</p>
    <p class="line line--note2">kindly give notice one day in advance.</p>
  </div>
</section>

<section class="card card--contact">
  <svg class="contact-shape" viewBox="0 0 686 390" aria-hidden="true">
    <path d="M218 0 C318 100 372 260 246 390 L686 390 L686 0 Z" fill="var(--green)"/>
    <path d="M228 0 C330 100 364 260 242 390 L686 390 L686 0 Z" fill="var(--white)"/>
    <path d="M235 0 C338 100 372 260 250 390 L686 390 L686 0 Z" fill="var(--brown)"/>
  </svg>
  <div class="brand-mark">
    <span class="brand-mark__dot"></span>
    <span class="brand-mark__name">Ferncliff</span>
  </div>
  <p class="person person__name">Marla Quintavelle</p>
  <p class="person person__title">Massage Therapist</p>
  <ul class="contact-list">
    <li>541-382-9147
      <svg viewBox="0 0 18 16"><path d="M2 6 Q9 0 16 6 L14 8 L12 6 L6 6 L4 8 Z"/><rect x="4" y="9" width="10" height="6" rx="1"/></svg></li>
    <li class="contact--email">Marla.Quintavelle@mailbox.example
      <svg viewBox="0 0 18 16"><rect x="1.5" y="3" width="15" height="10"/><path d="M1.5 3 L9 9 L16.5 3"/></svg></li>
    <li>FerncliffMassage.example
      <svg viewBox="0 0 18 16"><circle cx="9" cy="8" r="7"/><ellipse cx="9" cy="8" rx="3" ry="7"/><path d="M2 8 H16 M3 4.5 H15 M3 11.5 H15"/></svg></li>
  </ul>
  <p class="person person__license">LMT# 5186</p>
</section>

</body>
</html>
```